Crumb Joy pastry business card design

I need a logo and a business card design for my baking business, "Crumb Joy". I daily bake French pastries from scratch using high quality ingredients and directly cater to local customers. My product is very authentic but sold at a casual setting . I'm looking for a simple, cute, stylish yet earthy design. Like this kind of feel:
http://clipvista.example/71946302
Target Market(s)
Metropolitan food conscious consumers in their 20-40s
Industry/Entity Type
Business
Requirements
Must have
- Soft pastel colors or other types of color schemes that would remind French pastries.
email: welovecrumbles@mailnest.example
twitter@bitemesf
www.crumbjoyla.example
Nice to have
Should not have
- pictures of pastries - sketches are ok.

```html
<!DOCTYPE html>
<html lang="en">
<head>
<meta charset="utf-8">
<title>Crumb Joy – Business Card</title>
<link rel="stylesheet" href="https://fonts.googleapis.com/css2?family=Open+Sans:wght@400;600;700&display=swap">
<style>
  :root {
    --backdrop: #2a2a2a;
    --front-glow: #3a2a12;
    --front-edge: #1a1106;
    --brand-gold: #8a6128;
    --band-brown: #6e4b1c;
    --paper: #ffffff;
    --ink-brown: #5a3a12;
    --ink-dark: #2b1d0a;
    --divider: #3a2a16;
  }
  * { margin: 0; padding: 0; box-sizing: border-box; }
  html, body {
    width: 1200px;
    height: 900px;
    overflow: hidden;
    background: var(--backdrop);
    font-family: "Open Sans", Arial, sans-serif;
  }
  .canvas {
    position: relative;
    width: 1200px;
    height: 900px;
  }
  .card {
    position: absolute;
    top: 280px;
    width: 560px;
    height: 340px;
    box-shadow: 0 10px 30px rgba(0,0,0,0.5);
  }
  .card-front {
    left: 20px;
    background: radial-gradient(ellipse at 50% 45%, var(--front-glow) 0%, var(--front-edge) 75%);
    display: flex;
    align-items: center;
    justify-content: center;
  }
  .brand-name {
    font-size: 44px;
    font-weight: 400;
    color: var(--brand-gold);
    letter-spacing: 1px;
  }
  .card-back {
    left: 620px;
    background: var(--paper);
    border-top: 12px solid var(--band-brown);
    border-bottom: 12px solid var(--band-brown);
  }
  .back-brand {
    position: absolute;
    left: 30px;
    top: 140px;
    font-size: 30px;
    font-weight: 400;
    color: var(--ink-brown);
  }
  .divider {
    position: absolute;
    left: 272px;
    top: 80px;
    width: 3px;
    height: 160px;
    background: linear-gradient(to bottom, transparent, var(--divider) 50%, transparent);
  }
  .contact {
    position: absolute;
    left: 310px;
    top: 82px;
    color: var(--ink-brown);
    font-size: 12px;
    line-height: 1.15;
  }
  .contact-name {
    font-size: 16px;
    font-weight: 700;
  }
  .contact-role {
    font-size: 11px;
    font-weight: 700;
    margin-left: 6px;
    margin-bottom: 14px;
  }
  .contact-lines {
    margin-left: 14px;
    margin-bottom: 14px;
  }
  .contact-phones {
    margin-left: 14px;
  }
</style>
</head>
<body>
  <main class="canvas">
    <section class="card card-front" aria-label="Card front">
      <span class="brand-name">Crumb Joy</span>
    </section>

    <section class="card card-back" aria-label="Card back">
      <span class="back-brand">Crumb Joy</span>
      <div class="divider"></div>
      <div class="contact">
        <div class="contact-name">Your Name</div>
        <div class="contact-role">Position</div>
        <div class="contact-lines">
          <div>welovecrumbles@mailnest.example</div>
          <div>twitter@crumbjoyla</div>
          <div>www.crumbjoyla.example</div>
        </div>
        <div class="contact-phones">
          <div>555 010 2468</div>
          <div>(555) 010 135</div>
        </div>
      </div>
    </section>
  </main>
</body>
</html>
```